Owen Tasker Studios Business Card

Looking for a clear, modern, elegant, sharp business card that conveys a professional yet edgy image to my business as a wedding, portrait, and travel photographer. Would like something that looks vintage yet modern. Need a new business card to grow my business. We are growing the business for Wedding and Event Photography as well as fine art Photography. (Mostly Landscapes)
Updates

I’m looking through designs now but I have a new logo that i want using please.

New logo uploaded please redesign using that

PLEASE ALL DESIGNERS LOOK IN BRIEF FOR NEW LOGO

Target Market(s)

Brides, Grooms, Families with Kids, People looking for Fine Art Photography Artwork

Industry/Entity Type

Photographer

Contact Information for Business Card

Unsure

Font styles to use
Serif

Colors

Designer to choose colors to be used in the design.

Requirements
Must have
• My Website:
• http://taskerlens.examplefolio.net
• Phone:
• 323-481-5206
• Email:
• owentaskerlens@mailbox-example.net
Nice to have
• Would like a sort of shine on the printing finish.
• I like black I think it looks good on a business card.
• Can try working with my logo (png that I've attached)

```html
<!DOCTYPE html>
<html lang="en">
<head>
<meta charset="utf-8">
<title>Owen Tasker Studios — Business Card</title>
<link href="https://fonts.googleapis.com/css2?family=Montserrat:wght@400;600&display=swap" rel="stylesheet">
<style>
  :root {
    --backdrop: #dcdde0;
    --card-black: #151515;
    --card-black-light: #262626;
    --card-white: #ffffff;
    --ink-dark: #1a1a1a;
    --ink-light: #f2f2f2;
  }
  * { margin: 0; padding: 0; box-sizing: border-box; }
  html, body {
    width: 1200px; height: 962px; overflow: hidden;
    background: var(--backdrop);
    font-family: "Montserrat", sans-serif;
  }
  .canvas { position: relative; width: 1200px; height: 962px; }

  .card {
    position: absolute; left: 279px; width: 627px; height: 357px;
    overflow: hidden;
  }
  .card--front { top: 60px; }
  .card--back { top: 471px; background: var(--card-white); }

  .texture {
    position: absolute; inset: 0;
    background: linear-gradient(135deg, var(--card-black-light) 0%, var(--card-black) 55%, #0e0e0e 100%);
  }

  .wordmark {
    position: absolute; left: 0; right: 0; text-align: center;
    font-weight: 400;
  }
  .wordmark__name {
    display: block; font-size: 35px; letter-spacing: 0.13em; line-height: 1;
    padding-left: 0.13em;
  }
  .wordmark__sub {
    display: block; font-size: 13px; letter-spacing: 0.45em; line-height: 1;
    margin-top: 18px; padding-left: 0.45em;
  }
  .card--front .wordmark { top: 188px; color: var(--ink-light); }
  .card--back .wordmark { top: 85px; color: var(--ink-dark); }

  .contact-band {
    position: absolute; left: 0; right: 0; bottom: 0; height: 153px;
  }
  .contact-item {
    position: absolute; display: flex; align-items: center;
    color: var(--ink-light); font-weight: 600;
  }
  .contact-item svg { width: 36px; height: 36px; flex: none; margin-right: 11px; }
  .contact-item--email { left: 88px; top: 35px; font-size: 10px; letter-spacing: 0.02em; }
  .contact-item--phone { left: 88px; top: 89px; font-size: 12px; letter-spacing: 0.14em; font-weight: 400; }
  .contact-item--web { left: 352px; top: 35px; font-size: 10px; letter-spacing: 0.02em; }
</style>
</head>
<body>
<main class="canvas">

  <section class="card card--front">
    <div class="texture" role="img" aria-label="Dark geometric triangle pattern background"></div>
    <div class="wordmark">
      <span class="wordmark__name">OWEN TASKER</span>
      <span class="wordmark__sub">STUDIOS</span>
    </div>
  </section>

  <section class="card card--back">
    <div class="wordmark">
      <span class="wordmark__name">OWEN TASKER</span>
      <span class="wordmark__sub">STUDIOS</span>
    </div>
    <div class="contact-band">
      <div class="texture" role="img" aria-label="Dark geometric triangle pattern background"></div>

      <div class="contact-item contact-item--email">
        <svg viewBox="0 0 36 36" aria-hidden="true">
          <circle cx="18" cy="18" r="18" fill="#fff"/>
          <rect x="9" y="12" width="18" height="12" fill="#151515"/>
          <path d="M9 12 L18 19 L27 12" fill="none" stroke="#fff" stroke-width="1.4"/>
        </svg>
        <span>owentaskerlens@mailbox-example.net</span>
      </div>

      <div class="contact-item contact-item--phone">
        <svg viewBox="0 0 36 36" aria-hidden="true">
          <circle cx="18" cy="18" r="18" fill="#fff"/>
          <path d="M12.5 10 l3 -0.5 2 4.5 -2 1.5 c1 2.4 2.6 4 5 5 l1.5 -2 4.5 2 -0.5 3 c-0.5 1.5 -2 2 -3.5 1.7 C16.5 23.6 12.4 19.5 11 13.5 c-0.3 -1.5 0.2 -3 1.5 -3.5z" fill="#151515"/>
        </svg>
        <span>323-481-5206</span>
      </div>

      <div class="contact-item contact-item--web">
        <svg viewBox="0 0 36 36" aria-hidden="true">
          <circle cx="18" cy="18" r="18" fill="#fff"/>
          <circle cx="18" cy="18" r="9" fill="#151515"/>
          <path d="M14 12 c2 1 3 3 1.5 4.5 c-1.5 1.5 0 3 2 3.5 c1 2 -0.5 4 0 5.5 M21 11 c-1 2 1 3 3 3.5 c1.5 0.5 2 2 1.5 3.5" fill="none" stroke="#fff" stroke-width="1.6" stroke-linecap="round"/>
        </svg>
        <span>http://taskerlens.examplefolio.net</span>
      </div>
    </div>
  </section>

</main>
</body>
</html>
```